Christmas Flyer for Suburban London Cocktail Bar & Party Venue

We need a flyer with details of our Christmas Party drinks packages for party bookings. Tin and Thistle is a local cocktail bar with an emphasis on providing a modern hospitality environment with a sense of fun and whimsy. We pride ourselves on not being generic, providing a community atmosphere and don't take ourselves too seriously and our brand reflects that.

Christmas is one of the most popular times of year and we host parties for many people in our local area. The flyer is intended to summarise our promotional deals and will be distributed to local businesses as well as being available in the bar for customers.

An overview of our mood board that influences 'tone', as we await rebranding, can be seen at https://au.pinboardia.com/korvelmidge/commercial-bar-fit-out-inspiration/

Target Market(s)

21-35 Urban Professionals

Industry/Entity Type

Hospitality

Colors

Designer to choose colors to be used in the design.

Requirements
Must have
• The 4 offers contained in the copy text. Can be adjusted for legibility as long as the offers remain substantively the same.
• The logo of the bar. The standard logo is the gold version however that can be recoloured if appropriate.
• The Address Tin & Thistle - 27 Wrenmoor Rise - Balham, SW7 4KD - This need not be prominent.
Nice to have
• Our social media locations
• facebook /tinandthistlebar
• Instagram /tinandthistlebar
Should not have
• Should not contain photographs or exceptionally generic stock imagery.

```html
<!DOCTYPE html>
<html lang="en">
<head>
<meta charset="utf-8">
<title>Tin &amp; Thistle – Christmas Party Drinks Packages</title>
<link href="https://fonts.googleapis.com/css2?family=Stardos+Stencil:wght@400;700&family=Anton&family=Raleway:wght@400;500&display=swap" rel="stylesheet">
<style>
  :root{
    --backdrop:#8e8c8d;
    --charcoal:#2f2f2f;
    --navy:#13213f;
    --navy-deep:#0f1d3d;
    --red:#e41f26;
    --red-dark:#a3141a;
    --white:#ffffff;
    --text-soft:#e6e6e6;
    --wood-1:#5a3420;
    --wood-2:#2a1b14;
    --brick:#7e6f66;
    --bar-glow-1:#7a2a12;
    --bar-glow-2:#2a1208;
  }
  *{box-sizing:border-box;margin:0;padding:0}
  html,body{width:1200px;height:893px;overflow:hidden;background:var(--backdrop)}
  .canvas{position:relative;width:1200px;height:893px}
  .page{position:absolute;top:110px;width:476px;height:673px;overflow:hidden}
  .page--packages{left:103px;background:var(--charcoal)}
  .page--cover{left:622px;background:var(--charcoal)}

  /* Packages page */
  .packages-title{position:absolute;left:51px;top:40px;width:374px;text-align:center;
    font-family:"Stardos Stencil",serif;font-weight:700;font-variant:small-caps;
    color:var(--white);font-size:27px;line-height:26px;letter-spacing:.3px}
  .rule{position:absolute;left:51px;width:374px;height:2px;background:var(--white)}
  .bar-photo{position:absolute;background:radial-gradient(ellipse at 45% 65%,#d9542c 0%,var(--bar-glow-1) 28%,#4a2414 55%,var(--bar-glow-2) 100%)}
  .bar-photo--right{clip-path:polygon(14% 0,100% 0,100% 100%,0 100%)}
  .bar-photo--left{clip-path:polygon(0 0,86% 0,100% 100%,0 100%)}

  .offer-tag{position:absolute;width:128px;height:20px}
  .offer-tag svg{position:absolute;inset:0}
  .offer-tag span{position:relative;display:block;text-align:center;line-height:20px;
    font-family:"Stardos Stencil",serif;font-weight:700;font-variant:small-caps;
    color:var(--white);font-size:14px}
  .guest-count{position:absolute;width:40px;height:7px;background:var(--white);
    font-family:Anton,sans-serif;font-size:5px;line-height:7px;text-align:center;color:var(--navy)}

  .inclusions{position:absolute;list-style:none;font-family:Raleway,sans-serif;
    font-size:7.5px;color:var(--text-soft)}
  .inclusions li{height:14px;line-height:14px;white-space:nowrap}
  .inclusions li::before{content:"✓";margin-right:4px;color:var(--white)}
  .inclusions small{font-size:3.6px}
  .inclusions .col2{position:absolute;left:86px}

  .price{position:absolute;width:128px;height:48px}
  .price svg{position:absolute;inset:0}
  .price .amount{position:absolute;left:0;right:0;top:0;text-align:center;
    font-family:Anton,sans-serif;font-size:18px;line-height:22px;color:var(--white)}
  .price .saving{position:absolute;left:0;right:0;top:24px;text-align:center;
    font-family:Anton,sans-serif;font-size:11px;letter-spacing:1px;line-height:16px;color:var(--white)}

  /* Cover page */
  .cover-photo{position:absolute;inset:0;
    background:linear-gradient(160deg,var(--wood-1) 0%,#6b4128 22%,var(--brick) 38%,var(--wood-2) 60%,#3b3733 100%);
    clip-path:polygon(313px 0,476px 0,476px 266px,50px 673px,0 673px,0 310px)}
  .cover-band{position:absolute;inset:0;background:var(--navy-deep);
    clip-path:polygon(476px 266px,476px 673px,50px 673px)}
  .cover-frame{position:absolute;left:17px;top:17px;width:443px;height:641px;border:1.5px solid rgba(255,255,255,.85)}
  .brand-name{position:absolute;left:40px;top:62px;font-family:"Stardos Stencil",serif;
    font-weight:700;font-size:30px;color:var(--white);white-space:nowrap}
  .cover-tagline{position:absolute;right:55px;top:460px;text-align:right;
    font-family:"Stardos Stencil",serif;font-weight:700;font-variant:small-caps;
    color:var(--white);font-size:24px;line-height:32px}
</style>
</head>
<body>
<main class="canvas">

  <section class="page page--packages" aria-label="Christmas party drinks packages">
    <h1 class="packages-title">Christmas Party Drinks<br>Packages For Party Bookings</h1>
    <div class="rule" style="top:96px"></div>

    <!-- Sharing combo -->
    <div class="bar-photo bar-photo--right" style="left:197px;top:98px;width:228px;height:120px" role="img" aria-label="Photo of a sharing cocktail bowl in front of a lit back bar of bottles"></div>
    <div class="offer-tag" style="left:52px;top:110px">
      <svg viewBox="0 0 128 20" preserveAspectRatio="none"><polygon points="0,0 128,0 120,10 128,20 0,20 8,10" fill="var(--navy)"/></svg>
      <span>Sharing Combo</span>
    </div>
    <ul class="inclusions" style="left:52px;top:137px">
      <li>3 of our sharing cocktails</li>
      <li>Bottle of Prosecco</li>
    </ul>
    <div class="price" style="left:52px;top:165px">
      <svg viewBox="0 0 128 48"><path d="M28,24 A36,22 0 0 1 100,24 Z" fill="var(--navy)"/>
        <polygon points="0,18 12,16 14,36 2,38 6,28" fill="var(--red-dark)"/>
        <polygon points="128,18 116,16 114,36 126,38 122,28" fill="var(--red)"/>
        <path d="M8,18 Q64,30 120,18 L120,36 Q64,46 8,36 Z" fill="var(--red)"/></svg>
      <div class="amount">£85</div>
      <div class="saving">SAVE UP TO £35</div>
    </div>
    <div class="rule" style="top:218px"></div>

    <!-- Package 1 -->
    <div class="bar-photo bar-photo--left" style="left:51px;top:220px;width:238px;height:134px" role="img" aria-label="Photo of a sharing cocktail bowl in front of a lit back bar of bottles"></div>
    <div class="offer-tag" style="left:297px;top:233px">
      <svg viewBox="0 0 128 20" preserveAspectRatio="none"><polygon points="0,0 128,0 120,10 128,20 0,20 8,10" fill="var(--navy)"/></svg>
      <span>Xmas Package 1</span>
    </div>
    <div class="guest-count" style="left:341px;top:253px">10 PEOPLE</div>
    <ul class="inclusions" style="left:297px;top:263px">
      <li>10x Cocktails<span class="col2">✓ 10x Beers</span></li>
      <li>10x house spirit <small>- mixer, glass of wine or prosecco</small></li>
      <li>Bottle of prosecco</li>
    </ul>
    <div class="price" style="left:297px;top:306px">
      <svg viewBox="0 0 128 48"><path d="M28,24 A36,22 0 0 1 100,24 Z" fill="var(--navy)"/>
        <polygon points="0,18 12,16 14,36 2,38 6,28" fill="var(--red-dark)"/>
        <polygon points="128,18 116,16 114,36 126,38 122,28" fill="var(--red)"/>
        <path d="M8,18 Q64,30 120,18 L120,36 Q64,46 8,36 Z" fill="var(--red)"/></svg>
      <div class="amount">£150</div>
      <div class="saving">SAVE UP TO £65</div>
    </div>
    <div class="rule" style="top:354px"></div>

    <!-- Package 2 -->
    <div class="bar-photo bar-photo--right" style="left:197px;top:357px;width:228px;height:129px" role="img" aria-label="Photo of a sharing cocktail bowl in front of a lit back bar of bottles"></div>
    <div class="offer-tag" style="left:52px;top:367px">
      <svg viewBox="0 0 128 20" preserveAspectRatio="none"><polygon points="0,0 128,0 120,10 128,20 0,20 8,10" fill="var(--navy)"/></svg>
      <span>Xmas Package 2</span>
    </div>
    <div class="guest-count" style="left:96px;top:387px">15 PEOPLE</div>
    <ul class="inclusions" style="left:52px;top:396px">
      <li>15x Cocktails<span class="col2">✓ 15x Beers</span></li>
      <li>15x house spirit <small>- mixer, glass of wine or prosecco</small></li>
      <li>Sharing cocktail</li>
    </ul>
    <div class="price" style="left:52px;top:438px">
      <svg viewBox="0 0 128 48"><path d="M28,24 A36,22 0 0 1 100,24 Z" fill="var(--navy)"/>
        <polygon points="0,18 12,16 14,36 2,38 6,28" fill="var(--red-dark)"/>
        <polygon points="128,18 116,16 114,36 126,38 122,28" fill="var(--red)"/>
        <path d="M8,18 Q64,30 120,18 L120,36 Q64,46 8,36 Z" fill="var(--red)"/></svg>
      <div class="amount">£220</div>
      <div class="saving">SAVE UP TO £85</div>
    </div>
    <div class="rule" style="top:486px"></div>

    <!-- Package 3 -->
    <div class="bar-photo bar-photo--left" style="left:51px;top:488px;width:238px;height:142px" role="img" aria-label="Photo of a sharing cocktail bowl in front of a lit back bar of bottles"></div>
    <div class="offer-tag" style="left:297px;top:498px">
      <svg viewBox="0 0 128 20" preserveAspectRatio="none"><polygon points="0,0 128,0 120,10 128,20 0,20 8,10" fill="var(--navy)"/></svg>
      <span>Xmas Package 3</span>
    </div>
    <div class="guest-count" style="left:341px;top:518px">20 PEOPLE</div>
    <ul class="inclusions" style="left:297px;top:527px">
      <li>20x Cocktails<span class="col2">✓ 20x Beers</span></li>
      <li>20x house spirit <small>- mixer, glass of wine or prosecco</small></li>
      <li>Bottle of prosecco</li>
      <li>Treasure chest! <small>(12 Person Sharer valued at £100)</small></li>
    </ul>
    <div class="price" style="left:297px;top:584px">
      <svg viewBox="0 0 128 48"><path d="M28,24 A36,22 0 0 1 100,24 Z" fill="var(--navy)"/>
        <polygon points="0,18 12,16 14,36 2,38 6,28" fill="var(--red-dark)"/>
        <polygon points="128,18 116,16 114,36 126,38 122,28" fill="var(--red)"/>
        <path d="M8,18 Q64,30 120,18 L120,36 Q64,46 8,36 Z" fill="var(--red)"/></svg>
      <div class="amount">£350</div>
      <div class="saving">SAVE UP TO £150</div>
    </div>
    <div class="rule" style="top:630px"></div>
  </section>

  <section class="page page--cover" aria-label="Tin &amp; Thistle cover">
    <div class="cover-photo" role="img" aria-label="Photo of the bar interior: timber ceiling, pendant lamps, brick wall and a rustic sleeper-wood bar counter"></div>
    <div class="cover-band"></div>
    <div class="cover-frame"></div>
    <p class="brand-name">Tin &amp; Thistle</p>
    <p class="cover-tagline">Modern<br>Hospitality<br>Environment<br>With A Sense Of<br>Fun And Whimsy</p>
  </section>

</main>
</body>
</html>
```